Mouse and Rodent Infestation Spray

Need to Design label for 16oz bottle. The image sent has our initial design on it. Need other options.

Industry/Entity Type

Pest Control

Colors

Designer to choose colors to be used in the design.

```html
<!DOCTYPE html>
<html lang="en">
<head>
<meta charset="utf-8">
<title>Vermaway Mouse &amp; Rat Infestation Label</title>
<link rel="stylesheet" href="https://fonts.googleapis.com/css2?family=Passion+One:wght@700&family=Open+Sans:wght@400;800&family=Oswald:wght@500;600&display=swap">
<style>
  :root {
    --backdrop: #c9c9c9;
    --label-white: #f4f4f4;
    --green: #1f9a3c;
    --green-light: #6cbf45;
    --green-lime: #9ccc3a;
    --navy: #1f2a86;
    --red: #d0121b;
    --gold: #f5c518;
    --grey-text: #6a6a6a;
  }
  * { margin: 0; padding: 0; box-sizing: border-box; }
  html, body { width: 1200px; height: 1200px; overflow: hidden; background: var(--backdrop); }
  .label {
    position: absolute; left: 210px; top: 110px; width: 780px; height: 980px;
    background: var(--label-white); overflow: hidden;
    font-family: "Open Sans", sans-serif;
  }
  .brand-shield { position: absolute; left: 170px; top: 0; width: 440px; height: 260px; }
  .brand-name {
    position: absolute; left: 170px; top: 84px; width: 440px; text-align: center;
    font-family: "Open Sans", sans-serif; font-weight: 800; font-size: 48px; line-height: 1; letter-spacing: 4px;
    color: #fff;
  }
  .dots { position: absolute; left: 120px; width: 540px; border-top: 2px dotted var(--red); }
  .dots.top { top: 282px; }
  .dots.bottom { top: 460px; }
  .product-title {
    position: absolute; left: 0; top: 285px; width: 780px; text-align: center;
    font-family: "Passion One", sans-serif; font-weight: 700; font-size: 100px; line-height: 0.88;
    color: var(--navy); letter-spacing: 3px;
  }
  .chevron { position: absolute; left: 240px; top: 455px; width: 300px; height: 50px; }
  .usage {
    position: absolute; left: 0; top: 520px; width: 780px; text-align: center;
    font-size: 29px; color: var(--grey-text); letter-spacing: 0.5px;
  }
  .claims {
    position: absolute; left: 0; top: 585px; width: 780px;
    display: flex; justify-content: center; gap: 44px;
  }
  .claim {
    width: 110px; height: 110px; border-radius: 50%; background: var(--green);
    border: 3px solid #fff; box-shadow: 0 0 0 3px var(--green);
    display: flex; align-items: center; justify-content: center; text-align: center;
    font-family: "Oswald", sans-serif; font-weight: 500; font-size: 18px; line-height: 1.1; color: #fff;
  }
  .green-band { position: absolute; left: 0; top: 720px; width: 780px; height: 260px; }
  .emblem {
    position: absolute; left: 310px; top: 716px; width: 160px; height: 162px;
    background: linear-gradient(135deg, var(--green-lime), var(--navy) 55%, var(--red));
    clip-path: polygon(50% 0, 100% 14%, 96% 62%, 50% 100%, 4% 62%, 0 14%);
  }
  .bottom-row {
    position: absolute; left: 40px; top: 890px; width: 700px;
    display: flex; align-items: center; justify-content: space-between;
  }
  .formula-pill {
    display: flex; align-items: center; gap: 10px; background: var(--navy);
    border-radius: 30px; padding: 6px 20px 6px 8px;
    font-family: "Oswald", sans-serif; font-weight: 600; font-size: 22px; line-height: 1; color: var(--gold);
  }
  .bolt-disc { width: 52px; height: 52px; border-radius: 50%; background: #2c3aa8; display: flex; align-items: center; justify-content: center; }
  .volume-pill {
    background: var(--navy); color: #fff; border-radius: 20px; padding: 6px 20px;
    font-family: "Oswald", sans-serif; font-weight: 500; font-size: 20px;
  }
  .certs { display: flex; align-items: center; gap: 14px; }
  .cert-round { width: 60px; height: 60px; border-radius: 50%; background: #fff; border: 4px solid var(--navy); }
  .cert-square { width: 58px; height: 74px; border-radius: 6px; background: #fff; border: 3px solid #2f7ad1; }
</style>
</head>
<body>
<main class="label">
  <svg class="brand-shield" viewBox="0 0 440 260" aria-hidden="true">
    <defs>
      <linearGradient id="shieldFill" x1="0" y1="0" x2="1" y2="1">
        <stop offset="0" stop-color="#7cc24a"/>
        <stop offset="1" stop-color="#1f9a3c"/>
      </linearGradient>
    </defs>
    <path d="M0,0 H440 V150 L220,255 L0,150 Z" fill="url(#shieldFill)"/>
    <path d="M14,0 V142 L220,240 L426,142 V0" fill="none" stroke="#fff" stroke-width="3"/>
  </svg>
  <div class="brand-name">VERMAWAY</div>

  <div class="dots top"></div>
  <h1 class="product-title">MOUSE &amp; RAT<br>INFESTATION</h1>
  <div class="dots bottom"></div>
  <svg class="chevron" viewBox="0 0 300 50" aria-hidden="true">
    <path d="M0,8 H110 L150,30 L190,8 H300" fill="none" stroke="var(--navy)" stroke-width="5"/>
    <path d="M100,24 L150,44 L200,24" fill="none" stroke="var(--red)" stroke-width="3"/>
  </svg>

  <p class="usage">SAFE FOR INDOOR &amp; OUTDOOR USE</p>

  <div class="claims">
    <div class="claim">NATURAL<br>BAIT</div>
    <div class="claim">PESTICIDE<br>FREE</div>
    <div class="claim">LONG<br>LASTING</div>
  </div>

  <svg class="green-band" viewBox="0 0 780 260" preserveAspectRatio="none" aria-hidden="true">
    <defs>
      <linearGradient id="bandFill" x1="0" y1="0" x2="1" y2="0">
        <stop offset="0" stop-color="#9ccc3a"/>
        <stop offset="0.5" stop-color="#3aaa3f"/>
        <stop offset="1" stop-color="#1f9a3c"/>
      </linearGradient>
    </defs>
    <path d="M0,60 Q390,150 780,0 V260 H0 Z" fill="url(#bandFill)"/>
    <path d="M0,110 Q390,170 780,40 V260 H0 Z" fill="#1f9a3c" opacity="0.85"/>
  </svg>

  <div class="emblem" role="img" aria-label="Shield emblem with a crossed-out rat and lightning strokes"></div>

  <div class="bottom-row">
    <div class="formula-pill">
      <span class="bolt-disc">
        <svg width="28" height="36" viewBox="0 0 28 36" aria-hidden="true"><path d="M16,0 L2,20 H13 L9,36 L26,13 H15 Z" fill="var(--gold)"/></svg>
      </span>
      <span>ADVANCED<br>FORMULA</span>
    </div>
    <div class="volume-pill">16 OZ</div>
    <div class="certs">
      <div class="cert-round"></div>
      <div class="cert-square"></div>
    </div>
  </div>
</main>
</body>
</html>
```